Professional Speaker needs a Business Card Design

I am a Professional Speaker and I need a design for my business cards. I would like for it to look sleek and professional but not too busy or cluttered. The colors I need are a bright blue, middle level gray and white. I also want a picture on both the front and back of the card. I have somewhat of a design that I created but it's something very basic. I was having an issue with submitting my images to Kelbrook Press because they weren't able to get me the exact colors I wanted. I would like to stick with something similar to what I came up with but am open to viewing your ideas.
Industry/Entity Type
Business
Contact Information for Business Card
Please refer to word document attached. It should be file 5 and that contains all of the details I need on my card. Also please be sure and use my Logo that is attached. The file is named logo front.

```html
<!DOCTYPE html>
<html lang="en">
<head>
<meta charset="utf-8">
<title>Daniel Hayes – Business Cards</title>
<link rel="stylesheet" href="https://fonts.googleapis.com/css2?family=Marcellus&family=Marcellus+SC&display=swap">
<style>
  :root {
    --navy: #12306b;
    --royal: #2d4aa0;
    --bright-blue: #3ab3e8;
    --mid-gray: #b8b8b8;
    --ink: #0a0a0a;
    --paper: #ffffff;
    --stage: #3a3a3a;
    --photo-tone-a: #6b4a36;
    --photo-tone-b: #c9c6d4;
  }
  * { box-sizing: border-box; margin: 0; padding: 0; }
  html, body { width: 1200px; height: 516px; overflow: hidden; }
  body {
    background: var(--stage);
    font-family: "Marcellus", serif;
    position: relative;
  }
  .card {
    position: absolute;
    background: var(--paper);
    border: 3px solid var(--navy);
    overflow: hidden;
  }
  /* Front */
  .card-front { left: 132px; top: 190px; width: 430px; height: 200px; }
  .portrait-frame { position: absolute; left: 20px; top: 14px; width: 132px; height: 78px; }
  .portrait-frame .frame-back {
    position: absolute; inset: 4px 0 0 6px;
    background: var(--bright-blue); transform: rotate(-6deg);
  }
  .portrait-frame .frame-mid {
    position: absolute; inset: 2px 6px 2px 2px;
    background: var(--royal); transform: rotate(4deg);
  }
  .portrait-photo {
    position: absolute; inset: 6px 10px 6px 8px;
    background: linear-gradient(135deg, var(--photo-tone-a), var(--photo-tone-b));
  }
  .greeting { position: absolute; left: 172px; top: 24px; color: var(--navy); }
  .greeting .hi { font-size: 17px; line-height: 1; }
  .greeting .name { font-size: 29px; line-height: 1.1; }
  .role-band {
    position: absolute; left: 0; right: 0; top: 100px; height: 40px;
    background: var(--ink);
    color: var(--bright-blue);
    font-family: "Marcellus SC", serif;
    font-size: 18px; letter-spacing: 0.5px;
    display: flex; align-items: center; justify-content: center;
  }
  .motto-row {
    position: absolute; left: 0; right: 0; top: 142px; bottom: 0;
    display: flex; align-items: center; justify-content: space-between;
    padding: 0 12px;
  }
  .accent-mark { width: 26px; height: 26px; background: var(--royal); transform: rotate(45deg); }
  .motto { font-size: 44px; color: var(--royal); letter-spacing: 1px; }
  .motto .soft { color: var(--mid-gray); }
  /* Back */
  .card-back { left: 605px; top: 184px; width: 440px; height: 196px; }
  .brand { position: absolute; left: 140px; top: 16px; display: flex; align-items: center; gap: 8px; }
  .brand .dot { width: 14px; height: 14px; border-radius: 50%; background: var(--royal); }
  .brand .brand-name { font-size: 20px; color: var(--royal); }
  .title-block { position: absolute; left: 70px; width: 250px; top: 68px; text-align: center; color: var(--navy); }
  .title-block .title { font-size: 15px; line-height: 1.2; }
  .title-block .site { font-size: 13px; line-height: 1.2; }
  .contact-band {
    position: absolute; left: 0; right: 0; top: 120px; bottom: 0;
    background: var(--ink); color: var(--paper);
    font-size: 8.5px;
  }
  .social-row { position: absolute; left: 6px; top: 9px; display: flex; gap: 12px; align-items: center; }
  .social { display: flex; align-items: center; gap: 4px; }
  .social .marker { width: 14px; height: 14px; border: 1px solid var(--paper); border-radius: 50%; }
  .contact-line { position: absolute; left: 6px; top: 40px; display: flex; gap: 10px; }
  .contact-line .label { color: var(--bright-blue); }
  .standing-photo {
    position: absolute; right: 20px; top: 8px; width: 80px; height: 180px;
    background: linear-gradient(180deg, var(--photo-tone-b), #2a2a2a);
  }
</style>
</head>
<body>
  <section class="card card-front">
    <div class="portrait-frame">
      <div class="frame-back"></div>
      <div class="frame-mid"></div>
      <div class="portrait-photo" role="img" aria-label="Photo of Daniel Hayes speaking into a microphone"></div>
    </div>
    <div class="greeting">
      <p class="hi">Hi i'm</p>
      <p class="name">Daniel Hayes</p>
    </div>
    <div class="role-band">SPEAKER ~ AUTHOR ~ COACH</div>
    <div class="motto-row">
      <div class="accent-mark" role="img" aria-label="Blue diamond ornament"></div>
      <p class="motto">Love. <span class="soft">Live.</span> Life.</p>
      <div class="accent-mark" role="img" aria-label="Blue diamond ornament"></div>
    </div>
  </section>

  <section class="card card-back">
    <div class="brand">
      <span class="dot"></span>
      <span class="brand-name">Daniel Hayes</span>
    </div>
    <div class="title-block">
      <p class="title">CEO Hayes Unlimited</p>
      <p class="site">www.DanielHayesNow.com</p>
    </div>
    <div class="contact-band">
      <div class="social-row">
        <span class="social"><span class="marker"></span>Daniel Hayes</span>
        <span class="social"><span class="marker"></span>D.Hayes85</span>
        <span class="social"><span class="marker"></span>DanielHayes85</span>
        <span class="social"><span class="marker"></span>Daniel Hayes</span>
      </div>
      <div class="contact-line">
        <span>For Requests Contact:</span>
        <span><span class="label">Email:</span> info@danielhayesnow.com</span>
        <span><span class="label">Phone:</span> 555-014-2290</span>
      </div>
    </div>
    <div class="standing-photo" role="img" aria-label="Full-length photo of Daniel Hayes standing in a striped shirt"></div>
  </section>
</body>
</html>
```